Leading the way in online fitness and education requires power house web design

If you need to contact me you can do so via
skype: Travlin

We need a website designed for new company based in Houston Texas called "TravlinFit". We offer web based training and nutrition programs for our members for example we use the same software as these companies: http://marobelka.com/ http://www.liftquorra.com/ i would like my visitors to be captivated by the level of design creativity of the site.

colors to use would be grey, orange and green.
for example i like the green of this site http://www.cartbeam.com/
i will upload my logo files so you can get a feel for shades of grey and orange.

there is a 3d effect filter i would like applied to my logo for use in the web design i have uploaded what that effect looks like.

i will need your designs to be complete with all interior pages which will include Home, Fitness, Nutrition, Fit Lounge, Fit Score, Fit School, Contact Us, Sign up.

fit lounge on my site is the same as pathwick on liftquorra and locker room on marobelka just re branded.

fit school is a research corner for members to learn about health and fitness, we are members of major medical journals on health and fitness and will have all our articles be from the newest research findings.

competitor sites
these sites use same software:
http://marobelka.com/
http://www.liftquorra.com/

these sites are other software.
http://home.sprintmesa.com/software-for-athletes.aspx
http://www.vigordex.com/

here are some websites that i like:
http://www.crestwaveplay.com/
http://www.nub-lantern.com/
http://fimzol.com/
http://www.parqudo.com/
http://www.lortavi.de/fandiloop/
http://brisketmade.com/

i also like the greens in this site that i am uploading

I have been reviewing the designs and would like to update everyone at once I do not want a normal fitness website design style, no testimonials, blog post, bodyfat calculator

my website will be a membership based website. i want the website to sell the main points of my fitness app that my members will have access to look at the comments for my selling points, use those points in the site create designs and graphics to visualize those points.

look at these sites and gain inspiration

http://www.tuvelo.com.pl/#/projekty/case-studies
http://www.quendar.com/en#/home#ld-kpvm-402617-0045
http://www.nub-lantern.com/
http://fimzol.com/
http://www.parqudo.com/

i have a few designers asking me what the selling points are, the website needs to be built around these points

main selling points.

overview

programs utilize the best multi-joint exercises combined with high intensity cardio, to give you a full-body workout, efficiently and effectively. This means you’re burning more calories and building more lean muscle per unit of time than traditional weight training and cardio programs.

When you sign up, you''ll receive a work out and diet plan to fit your goals and fitness level. As you progress through your plan, you can use the personal fitness and meal calendar to record your results. When you sign-up we''ll ask you a series of questions and your workouts will be tailored to your exact needs. That means never having to use a generic diet and exercise plan again.

If you''ve ever tried to lose weight and build muscle and didn''t succeed, we feel your pain. Until now, trying to navigate all the fitness fads and latest trends on your own has been difficult. The best option - hiring a certified personal trainer - may be out of your financial reach. That''s where we come in - we''re personal trainers on a mission to help you reach your fitness goals quickly and for less money than in person training. Best of all, we''re here to help you day or night.

Fitness

Personal Fitness Calendar

Tailored to the member’s schedule and flexible to accommodate any changes to a member’s regular fitness schedule. Track your progress and stay on track with your fitness goals.

Custom Fitness Plan

Based on a member’s current physical condition and goals.

• Step by step exercise instructions
• 3-D video demonstrations of over 600 exercises, including functional and body-weight only movements
• Equipment filter can customize plans to your gym’s equipment package
• Record workouts to track exercise history and progression

Nutrition

Nutritional Assessment

Daily recommended caloric intake (Protein, Carbohydrates and Fats), based on personal profile and daily fitness plan.

Custom Meal Plan

Personalized meal plan based on nutritional assessment.

• Choose number of meals per day
• Add dietary restrictions, food preferences or dislikes
• Database of thousands of ingredients allows for hundreds of thousands of meal combinations
• Include favorite foods by entering custom nutritional information

Weight tracking

Calculate goal weight and track weight-loss or weight-gain progress. You will reach your goals in no time.

Fit Lounge

What is the most important part of any workout or fitness program? Staying motivated. And what better form of motivation than positive encouragement from your peers?

Fit Lounge is fitness focused social network for health-minded individuals looking for a simple and convenient place to track their workout goals and monitor their progress. A unique system of motivation, support and accountability makes setting fitness goals and then keeping up with them easy

Track

Start by setting fitness goals that you want to track. They can be anything from running and jogging to how many hours of sleep you are getting and how many glasses of water you are drinking every day. Other members of the travlinfits community might be tracking the same workout goals as you, so you can always join their groups as well.

Share

Once you start tracking your workout goals, you can share your progress with your friends. Reach a new max on your bench press? Let everyone know. Eclipse the 10 mile mark on your daily run? Spread the word! The communication of encouragement back and forth is a great way to ensure that everyone stays on track with their workout goals.

Achieve

Of course, the point of any workout or fitness program is to achieve the goals you’ve set. And with help from travlinfits workout tracking tools and encouragement from the community, you will achieve your workout goals in no time. When you see a friend has achieved his or her fitness goals, you can send them a virtual “fist bump” as a sign of congratulations. The number of “fist bumps” each user accumulates will be displayed on their profile, providing additional motivation and a healthy dose of competition.

Reason: i dont feel the designs i have received are of the quality i am looking for

check this website out, i know its flash, but i also know you can get creative without flash and have nice effects throughout the site.

http://www.driftlane-hub.com/

I dont want plain jane designs, insert the content i provided into the site and have it explored in a unique way. take as much time on the design as you need as i will keep extending deadline until i find one that is perfect.

as said before don't make the site anything like the competition sites, its only purpose is to sell the memberships using content provided so i need an innovative way to for them to explore that content,

as your designing this site add me on skype so i can detail and help brainstorm ideas my skype id is travlin
you can stray from the color scheme a little or throw it away if you want i just want to see how creative you can get.

Industry/Entity Type

School

Requirements
Nice to have
• if you notice at the bottom of http://marobelka.com/ she has the orange bar with the three short content parts, i like the idea of having a space like that for similar content.

on http://www.vigordex.com/ if you look to the left side of the scrolling icons i like the idea of having icons or animated pictures to point of key benefits.

```html
<!DOCTYPE html>
<html lang="en">
<head>
<meta charset="utf-8">
<title>TravlinFit – Home</title>
<link href="https://fonts.googleapis.com/css2?family=Oswald:wght@300;400;500&family=PT+Sans:wght@400;700&family=Russo+One&display=swap" rel="stylesheet">
<style>
:root{
  --page:#1f1f1f;
  --panel-2:#0c0c0c;
  --sheet:#ffffff;
  --band:#e3e3e3;
  --card:#f3f3f3;
  --green:#8cc63f;
  --green-dark:#3f6e0c;
  --green-light:#b7e35a;
  --orange:#f7941d;
  --orange-dark:#e0620c;
  --ink:#4a4a4a;
  --white:#ffffff;
  --footer-link:#a9a9a9;
}
*{box-sizing:border-box;margin:0;padding:0}
html,body{width:1200px;height:900px;overflow:hidden;background:var(--page);font-family:"PT Sans",Arial,sans-serif}
.canvas{position:relative;width:1200px;height:900px}
.abs{position:absolute}
h1,h2,h3,h4,h5{font-weight:400}
.utility-links{left:740px;top:4px;font-size:6px;color:var(--white);letter-spacing:.2px}
.sheet{left:344px;top:18px;width:513px;height:882px;background:var(--sheet)}
.header{left:344px;top:18px;width:513px;height:134px;background:linear-gradient(#161616,#0b0b0b)}
.brand{left:356px;top:32px;display:flex;align-items:center;gap:6px}
.brand-dot{width:26px;height:26px;border-radius:50%;background:var(--orange-dark)}
.brand-name{font-family:"Oswald",sans-serif;font-weight:500;font-size:24px;color:#c9c9c9;letter-spacing:.5px}
.social{top:51px;width:19px;height:19px;border-radius:50%;background:#dcdcdc;border:2px solid #f5f5f5}
.signup-btn{left:767px;top:52px;width:55px;height:18px;border-radius:9px;background:linear-gradient(var(--orange),var(--orange-dark));color:var(--white);font-family:"Oswald",sans-serif;font-size:11px;text-align:center;line-height:18px}
.nav-band{left:352px;top:98px;width:496px;height:42px;background:linear-gradient(#a9d066,#79a83a)}
.nav{left:0;top:113px;font-family:"Oswald",sans-serif;font-size:8.5px;color:var(--white)}
.nav span{position:absolute;white-space:nowrap}
.home-icon{left:384px;top:112px;width:13px;height:13px;border-radius:2px;background:var(--orange-dark)}
.search{left:714px;top:112px;width:104px;height:12px;border-radius:6px;background:#151515}
.hero-frame{left:352px;top:150px;width:496px;height:282px;background:var(--panel-2)}
.hero{left:360px;top:169px;width:471px;height:233px;background:linear-gradient(100deg,#0c1f03 0%,#2f5a08 18%,#7fbf14 42%,#c6ee4a 52%,#6aa512 64%,#2a5206 82%,#0a1a02 100%);overflow:hidden}
.hero-photo{position:absolute;right:0;top:0;width:145px;height:233px;background:linear-gradient(90deg,rgba(180,180,180,0) 0%,rgba(190,190,190,.6) 40%,rgba(150,150,150,.5) 100%)}
.hero-welcome{left:404px;top:184px;font-family:"Oswald",sans-serif;font-weight:300;font-size:23px;color:var(--white);letter-spacing:-.3px;white-space:nowrap}
.hero-pitch{left:407px;top:218px;font-family:"Russo One",sans-serif;font-size:16px;line-height:21px;color:var(--white);white-space:nowrap}
.hero-cta{left:397px;top:295px;width:57px;height:19px;border-radius:10px;background:linear-gradient(var(--green-light),#6aa512);color:var(--white);font-family:"Oswald",sans-serif;font-size:8px;text-align:center;line-height:19px}
.slide-dot{left:836px;width:7px;height:7px;border-radius:50%;background:#333}
.features{left:352px;top:432px;width:496px;height:133px;background:var(--band)}
.feature-icon{width:28px;height:28px;border-radius:4px;border:1px solid #bdbdbd;padding:5px;background:#f7f7f7}
.feature-icon span{display:block;width:100%;height:100%;border-radius:3px}
.feature-title{font-family:"Oswald",sans-serif;font-weight:400;font-size:17px;line-height:15px;color:var(--ink)}
.feature-text{width:145px;font-size:6.6px;line-height:10.5px;color:var(--ink)}
.more-btn{width:36px;height:18px;border-radius:9px;background:linear-gradient(#fafafa,#cfcfcf);box-shadow:0 3px 4px rgba(0,0,0,.25);font-family:"Oswald",sans-serif;font-size:8px;color:#222;text-align:center;line-height:18px}
.card{top:573px;width:150px;height:192px;border-radius:7px;background:var(--card)}
.mission-title{left:370px;top:586px;font-size:14px;color:#333}
.rule{height:1px;background:#d2d2d2}
.mission-lead{left:370px;top:619px;width:132px;font-size:6.2px;line-height:10.5px;font-weight:700;color:#333}
.mission-body{left:370px;top:669px;width:132px;font-size:6.2px;line-height:10.5px;color:var(--ink)}
.read-more{left:369px;top:740px;font-size:7px;font-weight:700;color:var(--green);border-bottom:1px dotted var(--green)}
.special{left:520px;background:#1a1a1a;overflow:hidden}
.special-title{left:528px;top:586px;font-family:"Oswald",sans-serif;font-size:15px;line-height:16px;color:var(--white)}
.special-list{left:529px;top:626px;font-size:6px;line-height:10.5px;font-weight:700;color:var(--white);list-style:none}
.register-btn{left:528px;top:661px;width:72px;height:18px;border-radius:9px;background:linear-gradient(var(--orange),var(--orange-dark));font-family:"Oswald",sans-serif;font-size:9px;color:var(--white);text-align:center;line-height:18px}
.package{left:620px;top:660px;font-family:"Oswald",sans-serif;font-size:11px;line-height:13px;color:#e9e0a0;text-align:center}
.special-photo{left:520px;top:684px;width:150px;height:81px;border-radius:0 0 7px 7px;background:linear-gradient(#2a2a2a,#5a5a5a 60%,#3a6a8a)}
.news-title{left:687px;top:586px;font-size:14px;color:#333}
.news-arrows{left:792px;top:588px;width:27px;height:15px;border-radius:7px;background:#2b2b2b}
.news-thumb{width:30px;height:46px;background:linear-gradient(#9ab6c8,#3d6a8a)}
.news-head{font-size:8px;color:#222}
.news-text{width:97px;font-size:4.6px;line-height:7px;color:#555;font-style:italic}
.footer{left:352px;top:775px;width:496px;height:125px;background:linear-gradient(#151515,#222)}
.footer-head{top:786px;font-family:"Oswald",sans-serif;font-weight:400;font-size:8px;color:var(--white);white-space:nowrap}
.footer-links{top:806px;font-size:5.2px;line-height:8px;color:var(--footer-link)}
.newsletter-head{left:720px;top:792px;font-size:8.5px;font-weight:700;color:var(--white)}
.newsletter-field{left:720px;top:816px;width:100px;height:17px;border-radius:9px;background:#1c1c1c;box-shadow:inset 0 1px 3px #000}
.newsletter-send{left:805px;top:815px;width:26px;height:19px;border-radius:9px;background:linear-gradient(#fafafa,#c9c9c9)}
.copyright{left:555px;top:884px;font-size:5.5px;color:var(--white)}
</style>
</head>
<body>
<div class="canvas">
  <div class="abs utility-links">Home | Contact us | Bookmark | Sitemap</div>
  <div class="abs sheet"></div>

  <header class="abs header"></header>
  <div class="abs brand"><span class="brand-dot"></span><span class="brand-name">TravlinFit</span></div>
  <span class="abs social" style="left:690px"></span>
  <span class="abs social" style="left:714px"></span>
  <span class="abs social" style="left:738px"></span>
  <div class="abs signup-btn">Signup</div>

  <div class="abs nav-band"></div>
  <span class="abs home-icon"></span>
  <nav class="abs nav">
    <span style="left:400px">HOME</span>
    <span style="left:443px">FITNESS</span>
    <span style="left:491px">NUTRITION</span>
    <span style="left:547px">FIT LOUNGE</span>
    <span style="left:600px">FIT SCORE</span>
    <span style="left:654px">FIT SCHOOL</span>
  </nav>
  <div class="abs search"></div>

  <section class="abs hero-frame"></section>
  <div class="abs hero" role="img" aria-label="Green light-streak background with a photo of a smiling fit man in jeans on the right">
    <div class="hero-photo"></div>
  </div>
  <h1 class="abs hero-welcome">Welcome to TravlinFit</h1>
  <p class="abs hero-pitch">Become a Member, We<br>will Manage your Fitness<br>Regeime!</p>
  <div class="abs hero-cta">Sign Up Now</div>
  <span class="abs slide-dot" style="top:171px;background:var(--green)"></span>
  <span class="abs slide-dot" style="top:182px"></span>
  <span class="abs slide-dot" style="top:193px"></span>

  <section class="abs features"></section>
  <div class="abs feature-icon" style="left:364px;top:447px"><span role="img" aria-label="Weightlifter icon" style="background:var(--orange-dark)"></span></div>
  <h2 class="abs feature-title" style="left:401px;top:454px">FITNESS</h2>
  <p class="abs feature-text" style="left:360px;top:484px">Lorem ipsum dolor sit amet, consectetuer adipiscing elit, sed diam nonummy nibh euis mod tincidunt ut laoreet dolore magn.</p>
  <div class="abs more-btn" style="left:363px;top:521px">More</div>

  <div class="abs feature-icon" style="left:522px;top:447px"><span role="img" aria-label="Green apple icon" style="background:#7db82a;border-radius:50%"></span></div>
  <h2 class="abs feature-title" style="left:559px;top:454px">NUTRITION</h2>
  <p class="abs feature-text" style="left:520px;top:484px">Lorem ipsum dolor sit amet, consectetuer adipiscing elit, sed diam nonummy nibh euis mod tincidunt ut laoreet dolore magn.</p>
  <div class="abs more-btn" style="left:523px;top:521px">More</div>

  <div class="abs feature-icon" style="left:683px;top:447px"><span role="img" aria-label="Stretching trainer icon" style="background:#4f9a2a"></span></div>
  <h2 class="abs feature-title" style="left:719px;top:448px">PERSONAL<br>TRAINING</h2>
  <p class="abs feature-text" style="left:681px;top:484px">Lorem ipsum dolor sit amet, consectetuer adipiscing elit, sed diam nonummy nibh euis mod tincidunt ut laoreet dolore magn.</p>
  <div class="abs more-btn" style="left:684px;top:521px">More</div>

  <article class="abs card" style="left:361px"></article>
  <h3 class="abs mission-title">Our Mission</h3>
  <div class="abs rule" style="left:370px;top:610px;width:130px"></div>
  <p class="abs mission-lead">Adipiscing elit, sed diam nonummy nib smod tincidunt ut laoreet dolore magnore a fiquam erat volutpatt wisi enim ad minim veniam.</p>
  <p class="abs mission-body">Quis nostrud exerci tation ullamcorper su scipit lobortis nisl ut aliquip exea commodo consequat. Duis autem vel eum iriure dolor in hendrerit in vulputate velitessem olestie consequat, vel illum dolore eu feugiat nulla facilisis at ve.</p>
  <a class="abs read-more">Read More</a>

  <article class="abs card special"></article>
  <h3 class="abs special-title">Membership<br>Special</h3>
  <svg class="abs" style="left:606px;top:574px" width="64" height="76" viewBox="0 0 64 76">
    <polygon points="32,0 38,10 50,4 50,17 63,16 56,28 64,38 54,45 60,58 47,58 44,72 34,63 24,74 20,60 6,63 10,49 0,40 9,31 3,19 16,18 16,5 27,11" fill="#c8ef3c"/>
    <text x="32" y="44" text-anchor="middle" font-family="Oswald, sans-serif" font-size="22" fill="#1a1a1a">$93</text>
  </svg>
  <ul class="abs special-list">
    <li>Club Plus Membership</li>
    <li>Freedom Membership</li>
    <li>Fitness Guides</li>
  </ul>
  <div class="abs register-btn">Register Now</div>
  <div class="abs package">Package<br>Offer</div>
  <div class="abs special-photo" role="img" aria-label="Photo of a smiling man and woman in workout clothes"></div>

  <article class="abs card" style="left:681px"></article>
  <h3 class="abs news-title">Fitness News</h3>
  <span class="abs news-arrows"></span>
  <div class="abs rule" style="left:687px;top:610px;width:132px"></div>
  <div class="abs news-thumb" style="left:688px;top:622px" role="img" aria-label="Photo of a boot camp workout"></div>
  <h4 class="abs news-head" style="left:723px;top:618px">Boot Camp</h4>
  <p class="abs news-text" style="left:723px;top:631px">Boot camp is one of the classic methods of building strength and endurance. Boot camp is a group activity for a small group of 5-10 members.</p>
  <div class="abs rule" style="left:687px;top:682px;width:132px"></div>
  <div class="abs news-thumb" style="left:688px;top:696px" role="img" aria-label="Photo of a personal training session"></div>
  <h4 class="abs news-head" style="left:723px;top:690px">Personal Training</h4>
  <p class="abs news-text" style="left:723px;top:703px">Our trainers are skilled in three different levels on the basis of their skill set, experience and commitment. Level 1 – This level training is best suited for beginners who need a steady start. This training will give the client a basic</p>

  <footer class="abs footer"></footer>
  <h5 class="abs footer-head" style="left:368px">Benefits of Membership</h5>
  <div class="abs footer-links" style="left:368px">Why Join<br>Testimonials<br>Group Fitness Classes<br>Leagues<br>Personal Training<br>Mobile Applications</div>
  <h5 class="abs footer-head" style="left:463px">Becoming a Member</h5>
  <div class="abs footer-links" style="left:463px">Join Now<br>Schedule a Tour</div>
  <h5 class="abs footer-head" style="left:548px">Corporate Memberships</h5>
  <div class="abs footer-links" style="left:548px">Information Request<br>Corporate Billing<br>Corporate Check-In</div>
  <h5 class="abs footer-head" style="left:643px">Member Tools</h5>
  <div class="abs footer-links" style="left:643px">Create an Account<br>My Account<br>My Club<br>Schedule Personal Training<br>Add a Family Member<br>Billing Information</div>
  <h5 class="abs newsletter-head">Newsletter Sign Up</h5>
  <div class="abs newsletter-field"></div>
  <div class="abs newsletter-send">
    <svg width="26" height="19" viewBox="0 0 26 19"><rect x="8" y="6" width="10" height="7" fill="none" stroke="#333" stroke-width="1"/><path d="M8 6 L13 10 L18 6" fill="none" stroke="#333" stroke-width="1"/></svg>
  </div>
  <p class="abs copyright">©2012 TravlinFit. All rights reserved.</p>
</div>
</body>
</html>
```